6' Banner Stands for exhibiting to Health Fairs with an audience of age 55+

We need designs for two 6' banner stands to stand on either side of our exhibition tables. We offer Hereditary Cancer Screening. I want the banners to have the same look and feel as the logo and the files color scheme logo, etc..

The Banners should have "Hereditary Cancer Screening" at the top with the Tag Line "The Test You Take For Them" underneath. A photo of grandparents with kids/grandkids and underneath the photos in large font one of the following messages:
1) "A Simple Swab Could Save A Family Members LIFE Get Tested Today!"
2) "Does Cancer Run In Your Family? Get Tested Today!"
3) "Knowledge Is Power" "Get Tested Today!"
4) "Will You Give Your Loved Ones The Information To Beat Cancer In Their Lives? Get Tested Today!
5) Knowledge Is Power Get Tested Today!"
Updates

Thank you all for your designs I now have the exact specs for the banners, so please use these as you update your designs. 31.5 inches X 83.25 inches and add a 1/2 inch bleed to all 4 sides. Thank you.

Target Market(s)

Persons 55+ who are grandparents

Industry/Entity Type

Healthcare

Font styles to use
Sans Serif
Other font styles liked:
• Comic Sans for "The Test You Take For Them"

Colors
9bcb3c
0356a4
ffffff

Requirements
Must have
• the main focus should be the hereditary cancer screening; "Hereditary Cancer Screening";
• "The test you order for them" in Comic Sans font underneath
• A photo or photos of grandparents with their grandchildren (multiple ethnicities)
• One of the slogans listed above
• GET TESTED TODAY underneath the messages at the bottom of the banner highlighted and eye catching
• www.kinhealthcheckup.net
Nice to have
• Logo at the top or bottom

```html
<!DOCTYPE html>
<html lang="en">
<head>
<meta charset="utf-8">
<title>Hereditary Cancer Screening Banner Stands</title>
<link rel="stylesheet" href="https://fonts.googleapis.com/css2?family=Montserrat:wght@600;700;800&family=Comic+Neue:wght@700&display=swap">
<style>
  :root {
    --navy: #101a4c;
    --brand-blue: #0356a4;
    --green: #8cc63f;
    --white: #ffffff;
    --backdrop: #d9dadd;
    --photo-warm: #d9b9a0;
    --photo-sky: #a9cfe6;
    --photo-sand: #e9dcc6;
    --photo-garden: #8ea86a;
  }
  * { box-sizing: border-box; margin: 0; padding: 0; }
  html, body { width: 1200px; height: 826px; overflow: hidden; }
  body {
    background: var(--backdrop);
    font-family: "Montserrat", Arial, sans-serif;
    position: relative;
  }
  .banner {
    position: absolute;
    top: 68px;
    width: 300px;
    height: 604px;
    background: var(--white);
    overflow: hidden;
    box-shadow: 0 2px 8px rgba(0,0,0,0.15);
  }
  .banner--family-gift { left: 62px; }
  .banner--family-history { left: 446px; }
  .banner--simple-swab { left: 831px; }
  .banner-art { position: absolute; inset: 0; width: 300px; height: 604px; }
  .brand {
    position: absolute;
    left: 0; right: 0;
    display: flex;
    align-items: center;
    justify-content: center;
    gap: 8px;
    color: var(--navy);
    font-weight: 700;
  }
  .brand-dot { border-radius: 50%; background: var(--navy); flex: none; }
  .brand-name { line-height: 0.95; letter-spacing: 0.5px; }
  .brand--large { top: 20px; }
  .brand--large .brand-dot { width: 46px; height: 46px; }
  .brand--large .brand-name { font-size: 17px; }
  .brand--small { top: 24px; }
  .brand--small .brand-dot { width: 36px; height: 36px; }
  .brand--small .brand-name { font-size: 13px; }
  .text-block {
    position: absolute;
    left: 0; right: 0;
    text-align: center;
    font-weight: 800;
    text-transform: uppercase;
  }
  .headline-stack { color: var(--navy); line-height: 1.05; }
  .headline-compact { top: 94px; font-size: 23px; letter-spacing: -0.3px; }
  .tagline {
    position: absolute;
    left: 0; right: 0;
    top: 160px;
    text-align: center;
    font-family: "Comic Neue", "Comic Sans MS", cursive;
    font-weight: 700;
    font-size: 15px;
    color: var(--green);
  }
  .headline-big { line-height: 0.98; }
  .headline-big .line-1 { font-size: 32px; display: block; }
  .headline-big .line-2 { font-size: 52px; display: block; letter-spacing: -0.5px; }
  .headline-big .line-3 { font-size: 36px; display: block; }
  .headline-big--top { top: 80px; color: var(--navy); }
  .headline-big--bottom { top: 442px; color: var(--white); }
  .swab-message { top: 86px; font-size: 20px; line-height: 1.2; color: var(--navy); letter-spacing: -0.3px; }
  .message {
    position: absolute;
    left: 0; right: 0;
    text-align: center;
    color: var(--white);
    font-weight: 700;
    font-size: 21px;
    line-height: 1.4;
    text-transform: uppercase;
  }
  .message--gift { top: 496px; }
  .message--history { top: 500px; line-height: 1.15; font-size: 22px; }
  .site-url {
    position: absolute;
    left: 0; right: 0;
    text-align: center;
    color: var(--green);
    font-weight: 700;
    font-size: 12.5px;
  }
  .site-url--gift { top: 578px; }
  .site-url--history, .site-url--swab { top: 572px; }
</style>
</head>
<body>

  <section class="banner banner--family-gift">
    <svg class="banner-art" viewBox="0 0 300 604" aria-hidden="false">
      <defs>
        <linearGradient id="gift-photo" x1="0" y1="0" x2="1" y2="1">
          <stop offset="0" stop-color="#ece3da"/>
          <stop offset="0.5" stop-color="#d9b9a0"/>
          <stop offset="1" stop-color="#6f86b3"/>
        </linearGradient>
      </defs>
      <path role="img" aria-label="Photo of laughing grandparents playing with their grandchildren" d="M0 205 C90 215 220 200 300 180 L300 470 L0 470 Z" fill="url(#gift-photo)"/>
      <path d="M0 196 C90 218 200 206 300 172 L300 184 C210 214 100 224 0 210 Z" fill="var(--green)"/>
      <path d="M0 448 C90 470 200 445 300 425 L300 604 L0 604 Z" fill="var(--navy)"/>
      <path d="M0 440 C90 462 200 437 300 417 L300 427 C200 447 90 472 0 450 Z" fill="var(--green)"/>
      <circle cx="44" cy="406" r="37" fill="var(--green)"/>
      <circle role="img" aria-label="Small photo of a family walking on a beach" cx="44" cy="406" r="31" fill="var(--photo-sand)"/>
      <circle cx="148" cy="396" r="40" fill="var(--green)"/>
      <circle role="img" aria-label="Small photo of a grandfather hugging his granddaughter" cx="148" cy="396" r="34" fill="var(--photo-warm)"/>
      <circle cx="254" cy="398" r="40" fill="var(--green)"/>
      <circle role="img" aria-label="Small photo of a family running across a park lawn" cx="254" cy="398" r="34" fill="var(--photo-garden)"/>
    </svg>
    <div class="brand brand--large">
      <span class="brand-dot"></span>
      <span class="brand-name">KINLINE<br>HEALTH<br>GROUP</span>
    </div>
    <h1 class="text-block headline-stack headline-compact">Hereditary<br>Cancer Screening</h1>
    <p class="tagline">"The Test You Take For Them"</p>
    <p class="message message--gift">Give Them The Gift<br>Of Knowledge</p>
    <p class="site-url site-url--gift">www.kinhealthcheckup.net</p>
  </section>

  <section class="banner banner--family-history">
    <svg class="banner-art" viewBox="0 0 300 604">
      <defs>
        <linearGradient id="history-photo" x1="0" y1="0" x2="0" y2="1">
          <stop offset="0" stop-color="#ffffff"/>
          <stop offset="0.25" stop-color="#a9cfe6"/>
          <stop offset="0.5" stop-color="#5e93b8"/>
          <stop offset="0.7" stop-color="#e9dcc6"/>
          <stop offset="1" stop-color="#d8c6a8"/>
        </linearGradient>
      </defs>
      <rect role="img" aria-label="Photo of grandparents walking hand in hand with a grandchild along a beach" x="0" y="196" width="300" height="300" fill="url(#history-photo)"/>
      <path d="M0 466 C100 484 210 478 300 458 L300 604 L0 604 Z" fill="var(--green)"/>
      <path d="M0 474 C100 492 210 486 300 466 L300 604 L0 604 Z" fill="var(--navy)"/>
    </svg>
    <div class="brand brand--small">
      <span class="brand-dot"></span>
      <span class="brand-name">KINLINE<br>HEALTH<br>GROUP</span>
    </div>
    <h1 class="text-block headline-big headline-big--top">
      <span class="line-1">Hereditary</span>
      <span class="line-2">Cancer</span>
      <span class="line-3">Screening</span>
    </h1>
    <p class="message message--history">Does Cancer Run<br>In Your Family?</p>
    <p class="site-url site-url--history">www.kinhealthcheckup.net</p>
  </section>

  <section class="banner banner--simple-swab">
    <svg class="banner-art" viewBox="0 0 300 604">
      <defs>
        <linearGradient id="swab-photo" x1="0" y1="0" x2="0" y2="1">
          <stop offset="0" stop-color="#ffffff"/>
          <stop offset="0.15" stop-color="#b9c79e"/>
          <stop offset="0.45" stop-color="#8ea86a"/>
          <stop offset="0.75" stop-color="#dcb7b4"/>
          <stop offset="1" stop-color="#c7aab0"/>
        </linearGradient>
      </defs>
      <rect role="img" aria-label="Photo of smiling grandparents sitting in a garden with their two grandchildren" x="0" y="150" width="300" height="280" fill="url(#swab-photo)"/>
      <path d="M0 400 C100 416 210 410 300 388 L300 604 L0 604 Z" fill="var(--green)"/>
      <path d="M0 408 C100 424 210 418 300 396 L300 604 L0 604 Z" fill="var(--navy)"/>
    </svg>
    <div class="brand brand--small">
      <span class="brand-dot"></span>
      <span class="brand-name">KINLINE<br>HEALTH<br>GROUP</span>
    </div>
    <p class="text-block swab-message">A Simple Swab<br>Could Save A Family<br>Members Life</p>
    <h1 class="text-block headline-big headline-big--bottom">
      <span class="line-1">Hereditary</span>
      <span class="line-2">Cancer</span>
      <span class="line-3">Screening</span>
    </h1>
    <p class="site-url site-url--swab">www.kinhealthcheckup.net</p>
  </section>

</body>
</html>
```